HIgh-end jewelry designer needs a business card design

I need a business card design for the ecclectic & rather expensive jewelry designs. My approach to my work is to combine very old jewelry offset with contemporary items. I enjoy the idea of legacy as well as repurposing finely crafted items that are not possible to create any longer. My desire is to celebrate the past in a contemporary & funky way. The name of my business is VELLORINE. I see my business card design as simple & yet enigmatic as possible. In the end... clean, simple & understated is the look I am after. Thank you for your consideration...

Target Market(s)

I will use this business card for the trade as well as customers

Industry/Entity Type

Business

Contact Information for Business Card

Marta Quorrin Owner/Designer 555-203-7718

Requirements
Must have
• Clean & simple sophisticated design using the word "Vellorinne" as the logo. I like the idea of a play on the word itself, perhaps even using different fonts (i.e.: a bold helvetica combined with a lovely script). I'm afraid to say more because I don't want to limit creative input. Gosh, sometimes it's ok to break the rules!
Nice to have
• In my mind, I have imagined this business card to be simple, using my company name "Vellorine" in a playful yet sophisticated manner. I believe that doing something beautifully simple can be a true challenge. I have imagined something with just black & white, however I am open to ideas... after all that's why I'm here!
Should not have
• As Mozart once said... "It has too many notes!" I know I'm being silly, but I don't want it to be complicated or overly ornate.

```html
<!DOCTYPE html>
<html lang="en">
<head>
<meta charset="utf-8">
<title>Vellorine — Business Card</title>
<link rel="stylesheet" href="https://fonts.googleapis.com/css2?family=Bodoni+Moda:opsz,wght@6..96,400&display=swap">
<style>
  :root {
    --ink: #0b0b0b;
    --paper: #ffffff;
  }
  html, body {
    margin: 0;
    padding: 0;
    width: 1200px;
    height: 702px;
    overflow: hidden;
    background: var(--paper);
  }
  .card {
    display: block;
    width: 1200px;
    height: 702px;
  }
  .card text {
    font-family: "Bodoni Moda", "Bodoni 72", "Didot", serif;
    font-weight: 400;
  }
  .half--light { fill: var(--paper); }
  .half--dark { fill: var(--ink); }
  .wordmark { font-size: 192px; }
  .wordmark--on-light { fill: var(--ink); }
  .wordmark--on-dark { fill: var(--paper); }
  .contact { fill: var(--paper); }
  .contact__name { font-size: 58px; }
  .contact__role { font-size: 30px; }
  .contact__line { font-size: 44px; }
</style>
</head>
<body>
<svg class="card" viewBox="0 0 1200 702" xmlns="http://www.w3.org/2000/svg" role="img" aria-label="Vellorine business card for Marta Quorrin">
  <defs>
    <clipPath id="clip-light"><rect x="0" y="0" width="574" height="702"/></clipPath>
    <clipPath id="clip-dark"><rect x="574" y="0" width="626" height="702"/></clipPath>
  </defs>

  <rect class="half--light" x="0" y="0" width="574" height="702"/>
  <rect class="half--dark" x="574" y="0" width="626" height="702"/>

  <g class="wordmark-group">
    <text class="wordmark wordmark--on-light" x="585" y="192" text-anchor="middle" clip-path="url(#clip-light)">Vellorine</text>
    <text class="wordmark wordmark--on-dark" x="585" y="192" text-anchor="middle" clip-path="url(#clip-dark)" aria-hidden="true">Vellorine</text>
  </g>

  <g class="contact">
    <text class="contact__name" x="839" y="354" text-anchor="middle">Marta Quorrin</text>
    <text class="contact__role" x="1017" y="387" text-anchor="end">owner/designer</text>
    <text class="contact__line contact__phone" x="836" y="505" text-anchor="middle">P: 555.203.7718</text>
    <text class="contact__line contact__email" x="835" y="553" text-anchor="middle">mquorrin@vellorine.co</text>
  </g>
</svg>
</body>
</html>
```